Domainer Needs a Wordpress Company Website

I need a wordpress design for a new small business in Portland, Or called Tulvex .com . I want to put the growing collection of virtual real estate /domains online for sale to end-users, small businesses, and other local stakeholders. Basically a portfolio website with cashlume link for immediate payment and then confirmed info is returned to Owner:Tulvex, Inc..

I would like to use previously purchased roster of wordpress plugins from QX Lantern.net that would incorporate into this company design. Some of the plugins to spread the word and social media concerns. It would be zipped file to you of course.

I do have a collection of wordpress themes from BrisklyMotifs.com that are interesting. If interested.

Basically, I need someone to take the pieces I supply and make a wordpress website thats allows cashlume payments. A couple of forms to be sent. A website that allows me to list the virtual properties and accepts potential clients request for more information and/or their payments to cashlume for a domain.
Im committed to : white space on all pages. html5 complied . cashlume. , listing several 100's domains to sell on this handcrafted website of yours.

Target Market(s)

mom and pop local business, local and regional businesses, end users, marketing agency, marketing groups, product groups, national producers,
Professionals. Clients. Teachers and students. Domainers.

Industry/Entity Type

Real Estate

Font styles to use
Sans Serif

Colors
f78f20
f68e4e
fabb94
f04a50
00a98f
ffffff

Requirements
Must have
• Company website. Easy to look at, easy to read.
Instilling projecting that professionals are behind this website.
Class. Exclusive maybe.
Pages: home, who are we, domains, contact, faq, blog, .
Cashlume link. Confirmation page to Tulvex, Inc stating payment for said domain or hosting.

White Space , Gold , gold muted , type colors. Greens. Shades of Blues
Should not have
• Dark pages.
Sloppy pages.
Pages that don't shift synchronize.
non professionalism looks or outdated photos, models, fonts.

```html
<!DOCTYPE html>
<html lang="en">
<head>
<meta charset="utf-8">
<title>Tulvex — Domain Registration</title>
<link href="https://fonts.googleapis.com/css2?family=Open+Sans:wght@400;600;700&family=Oswald:wght@400;500&display=swap" rel="stylesheet">
<style>
:root{
  --orange:#f78f20;
  --coral:#f68e4e;
  --peach:#fabb94;
  --red:#f04a50;
  --green:#00a98f;
  --white:#ffffff;
  --ink:#333333;
  --muted:#777777;
  --line:#dddddd;
  --panel:#f2f2f2;
  --slate:#4d5257;
  --page:#e9e9e9;
}
*{box-sizing:border-box;margin:0;padding:0}
html,body{width:880px;height:1200px;overflow:hidden}
body{background:var(--page);font-family:"Open Sans",Arial,sans-serif;color:var(--ink);font-size:11px}
.site{width:800px;height:1200px;margin:0 auto;background:var(--white);position:relative}

/* header */
.header{height:78px;display:flex;align-items:center;justify-content:space-between;padding:0 24px;border-bottom:1px solid var(--line)}
.brand{display:flex;align-items:center;gap:8px}
.brand-mark{width:14px;height:14px;background:var(--orange)}
.brand-name{font-size:28px;font-weight:700;color:var(--orange);line-height:1}
.brand-tag{font-size:8px;color:var(--muted);margin-top:2px}
.nav{display:flex;gap:18px;font-size:10px;text-transform:uppercase;color:var(--muted)}
.nav a{color:inherit;text-decoration:none}
.nav .is-active{color:var(--red);border-bottom:2px solid var(--red);padding-bottom:3px}

/* hero */
.hero{height:250px;margin:12px 24px 0;background:linear-gradient(#fafafa,#ececec);display:flex;padding:28px 24px;position:relative;border-top:3px solid var(--red)}
.hero-copy{width:380px}
.hero-title{font-size:22px;color:var(--red);font-weight:600}
.hero-text{font-size:10px;color:var(--muted);margin-top:8px;line-height:1.5}
.hero-find{font-size:13px;font-weight:700;margin-top:28px}
.search{display:flex;margin-top:10px}
.search-input{width:250px;height:36px;border:1px solid var(--line);background:var(--white);padding:0 12px;font-size:14px;color:#aaa;display:flex;align-items:center}
.search-btn{width:80px;height:36px;background:var(--green);color:var(--white);font-weight:700;display:flex;align-items:center;justify-content:center;font-size:11px}
.hero-art{position:absolute;right:24px;top:20px;width:300px;height:215px;border-radius:4px;background:linear-gradient(160deg,#d8e8f5,#f0f4f8 55%,#7fb441 80%,#4e8a2a)}

/* plans */
.plans{display:flex;gap:10px;margin:24px 24px 0}
.plan{flex:1;height:90px;display:flex;align-items:center;justify-content:space-between;padding:0 16px;color:var(--white)}
.plan--bronze{background:var(--red)}
.plan--silver{background:var(--orange)}
.plan--gold{background:var(--panel);color:var(--ink);border:1px solid var(--line)}
.plan-name{font-family:Oswald,sans-serif;font-size:20px}
.plan-name b{font-weight:500}
.plan-desc{font-size:8px;line-height:1.4;margin-top:4px;max-width:120px;text-transform:uppercase}
.plan-price{width:60px;height:60px;border-radius:6px;background:rgba(255,255,255,.25);display:flex;flex-direction:column;align-items:center;justify-content:center;font-family:Oswald,sans-serif;font-size:18px}
.plan--gold .plan-price{background:var(--slate);color:var(--white)}
.plan-price small{font-size:8px;font-family:"Open Sans",sans-serif}

/* wish list */
.wish{margin:22px 24px 0}
.section-title{font-size:15px;font-weight:700;color:var(--ink)}
.wish-body{display:flex;gap:14px;margin-top:12px;align-items:flex-start}
.ext-grid{display:grid;grid-template-columns:repeat(5,1fr);gap:4px;width:330px}
.ext-grid--small{width:150px;grid-template-columns:repeat(3,1fr)}
.ext{height:22px;border:1px solid var(--line);font-size:8px;color:var(--muted);display:flex;align-items:center;justify-content:center}
.wish-label{font-size:22px;font-family:Oswald,sans-serif;width:70px;line-height:1.1;padding-top:20px}
.wish-art{width:80px;height:80px;background:linear-gradient(135deg,var(--peach),var(--coral));border-radius:4px}
.view-all{width:60px;height:56px;background:var(--orange);color:var(--white);display:flex;align-items:center;justify-content:center;font-weight:700;font-size:10px}

/* services */
.mid{display:flex;gap:24px;margin:24px 24px 0}
.services{width:230px}
.services .section-title{color:var(--red);font-family:Oswald,sans-serif;font-weight:400;font-size:20px}
.list{list-style:none;margin-top:12px}
.list li{font-size:9px;padding:7px 0 7px 12px;border-bottom:1px solid var(--line);position:relative}
.list li::before{content:"";position:absolute;left:2px;top:11px;width:4px;height:4px;background:var(--orange)}
.popular{flex:1}
.popular .section-title{color:var(--red);font-weight:600;font-size:14px}
.tld-board{margin-top:10px;background:var(--slate);border-radius:4px;padding:14px;display:grid;grid-template-columns:repeat(5,1fr);gap:8px}
.tld{height:20px;background:rgba(255,255,255,.08);color:#ddd;font-size:9px;display:flex;align-items:center;padding-left:8px}

/* footer */
.footer{position:absolute;left:0;right:0;top:930px;height:240px;background:var(--panel);display:flex;padding:20px 24px;gap:24px;border-top:1px solid var(--line)}
.footer-col{width:220px}
.footer-col h3{font-size:13px;font-weight:600}
.socials{display:flex;gap:5px;margin-top:16px}
.social{width:14px;height:14px;background:var(--slate)}
.footer-art{flex:1;border-radius:4px;background:linear-gradient(135deg,var(--peach),var(--red))}
.bottom{position:absolute;left:0;right:0;bottom:0;height:30px;background:var(--white);display:flex;justify-content:space-between;align-items:center;padding:0 24px;font-size:8px;color:var(--muted)}
</style>
</head>
<body>
<div class="site">
  <header class="header">
    <div class="brand">
      <span class="brand-mark"></span>
      <div>
        <div class="brand-name">Tulvex</div>
        <div class="brand-tag">Your Trusted Domain Marketplace</div>
      </div>
    </div>
    <nav class="nav">
      <a class="is-active">Home</a><a>Who are we</a><a>Domain</a><a>Contact</a><a>FAQ</a><a>Blog</a>
    </nav>
  </header>

  <section class="hero">
    <div class="hero-copy">
      <h1 class="hero-title">Domain registration</h1>
      <p class="hero-text">We offer our clients fast and effective domain name registration services that help you to expand your online business without compromising your expectations.</p>
      <p class="hero-find">Start to find your domain name</p>
      <div class="search">
        <div class="search-input">Search for a new domain</div>
        <div class="search-btn">SEARCH</div>
      </div>
    </div>
    <div class="hero-art" role="img" aria-label="Colourful domain extension signs standing on a patch of grass"></div>
  </section>

  <section class="plans">
    <div class="plan plan--bronze">
      <div><div class="plan-name"><b>BRONZE</b> Plan</div><div class="plan-desc">Free web registration, fast domain transfer, 24/7 live support</div></div>
      <div class="plan-price">$12.9<small>month</small></div>
    </div>
    <div class="plan plan--silver">
      <div><div class="plan-name"><b>SILVER</b> Plan</div><div class="plan-desc">Free web registration, fast domain transfer, 24/7 live support</div></div>
      <div class="plan-price">$17.9<small>month</small></div>
    </div>
    <div class="plan plan--gold">
      <div><div class="plan-name"><b>GOLDEN</b> Plan</div><div class="plan-desc">Free web registration, fast domain transfer, 24/7 live support</div></div>
      <div class="plan-price">$21.9<small>month</small></div>
    </div>
  </section>

  <section class="wish">
    <h2 class="section-title">Build your own wish list by selecting specific extensions</h2>
    <div class="wish-body">
      <div class="ext-grid">
        <div class="ext">.lighting</div><div class="ext">.land</div><div class="ext">.estate</div><div class="ext">.email</div><div class="ext">.guru</div>
        <div class="ext">.photos</div><div class="ext">.builders</div><div class="ext">.house</div><div class="ext">.property</div><div class="ext">.design</div>
        <div class="ext">.club</div><div class="ext">.homes</div><div class="ext">.ventures</div><div class="ext">.rentals</div><div class="ext">.city</div>
        <div class="ext">.gallery</div><div class="ext">.today</div><div class="ext">.build</div><div class="ext">.space</div><div class="ext">.agency</div>
      </div>
      <div class="wish-label">Real Estate</div>
      <div class="wish-art" role="img" aria-label="Small house model held in hands"></div>
      <div class="ext-grid ext-grid--small">
        <div class="ext">.villas</div><div class="ext">.condos</div><div class="ext">.realty</div>
        <div class="ext">.place</div><div class="ext">.farm</div><div class="ext">.lease</div>
        <div class="ext">.home</div><div class="ext">.town</div><div class="ext">.plus</div>
      </div>
      <div class="view-all">View all</div>
    </div>
  </section>

  <section class="mid">
    <div class="services">
      <h2 class="section-title">Our Services</h2>
      <ul class="list">
        <li>Domain Registration</li><li>Domain Renewal</li><li>Transfer Domains to Tulvex</li>
        <li>Free Domain Services</li><li>Private Registration</li><li>Domain Pricing</li><li>All Domain Extensions</li>
      </ul>
    </div>
    <div class="popular">
      <h2 class="section-title">Popular new domain extentions</h2>
      <div class="tld-board">
        <div class="tld">.com</div><div class="tld">.net</div><div class="tld">.org</div><div class="tld">.biz</div><div class="tld">.info</div>
        <div class="tld">.eu</div><div class="tld">.de</div><div class="tld">.us</div><div class="tld">.co</div><div class="tld">.me</div>
        <div class="tld">.tv</div><div class="tld">.mobi</div><div class="tld">.pro</div><div class="tld">.name</div><div class="tld">.asia</div>
        <div class="tld">.club</div><div class="tld">.shop</div><div class="tld">.site</div><div class="tld">.online</div><div class="tld">.store</div>
        <div class="tld">.tech</div><div class="tld">.blog</div><div class="tld">.live</div><div class="tld">.world</div><div class="tld">.life</div>
        <div class="tld">.news</div><div class="tld">.media</div><div class="tld">.global</div><div class="tld">.zone</div><div class="tld">.one</div>
      </div>
    </div>
  </section>

  <footer class="footer">
    <div class="footer-col">
      <h3>Domains</h3>
      <ul class="list">
        <li>Domain Registration</li><li>Domain Renewal</li><li>Transfer Domains to Tulvex</li><li>Free Domain Services</li><li>Private Registration</li>
      </ul>
    </div>
    <div class="footer-col">
      <h3>Support</h3>
      <ul class="list">
        <li>Support center</li><li>Popular How-Tos</li><li>Lost Password</li><li>Find Account Sign-in</li>
      </ul>
      <div class="socials"><span class="social"></span><span class="social"></span><span class="social"></span><span class="social"></span><span class="social"></span></div>
    </div>
    <div class="footer-art" role="img" aria-label="Red three-dimensional real estate lettering with a roof"></div>
  </footer>
  <div class="bottom"><span>Tulvex, Inc © All Rights Reserved</span><span>Terms of Use · Privacy Policy</span></div>
</div>
</body>
</html>
```